Ordner für Schulungsunterlagen
Zielgruppe
Die stahlwerk Akademie bietet verschiedene Schulungen in den Bereichen Arbeitssicherheit und Brandschutz an.
Aufgabenstellung
Ich möchte gerne für unsere Schulungen Ordner mit einem ansprechenden Design entwerfen lassen. Es sollte sowohl mit Arbeitssicherheit, als auch mit Brandschutz zu tun haben.
Angaben zum Ordner:
- Hebelordner DIN A 4
- Füllhöhe 55mm und 30mm
- mit 2 Ringen
- mit Schlitzösen
- mit Griffloch
- mit Dreiecktasche
- Bedruckung nur auf der Außenseite
- mit Entwurf für Register

```html
<!DOCTYPE html>
<html lang="de">
<head>
<meta charset="utf-8">
<title>stahlwerk Akademie – Ordner</title>
<link rel="stylesheet" href="https://fonts.googleapis.com/css2?family=Exo+2:wght@400;500;600&family=Caveat:wght@500&display=swap">
<style>
  :root {
    --navy: #313f68;
    --red: #c1151f;
    --white: #ffffff;
    --ink: #2b3558;
    --brand-blue: #2c3591;
  }
  html, body {
    margin: 0;
    padding: 0;
    width: 1200px;
    height: 602px;
    overflow: hidden;
    background: var(--white);
  }
  .cover {
    position: relative;
    width: 1200px;
    height: 602px;
    font-family: "Exo 2", sans-serif;
  }
  .cover-shapes { position: absolute; inset: 0; }
  .brand {
    position: absolute;
    right: 90px;
    top: 176px;
    display: flex;
    align-items: center;
    gap: 8px;
    color: var(--brand-blue);
    font-size: 24px;
    font-weight: 500;
    line-height: 1;
    white-space: nowrap;
  }
  .brand-dot {
    width: 18px;
    height: 18px;
    border-radius: 50%;
    background: var(--red);
    flex: none;
  }
  .tagline {
    position: absolute;
    right: 84px;
    top: 222px;
    white-space: nowrap;
    font-family: "Caveat", cursive;
    font-size: 18px;
    font-weight: 500;
    line-height: 1;
    color: var(--brand-blue);
  }
  .claim {
    position: absolute;
    right: 81px;
    top: 505px;
    text-align: right;
    color: var(--white);
    font-size: 12.5px;
    line-height: 15px;
    letter-spacing: 0.02em;
  }
  .claim .accent { color: var(--red); }
  .contact {
    position: absolute;
    left: 201px;
    top: 361px;
    color: var(--ink);
    font-size: 7.4px;
    font-weight: 500;
  }
  .contact-row {
    display: flex;
    align-items: flex-start;
    gap: 7px;
    margin-bottom: 10px;
    line-height: 9px;
  }
  .contact-icon { width: 11px; height: 11px; flex: none; fill: var(--ink); }
</style>
</head>
<body>
<div class="cover">
  <svg class="cover-shapes" viewBox="0 0 1200 602" width="1200" height="602">
    <defs>
      <linearGradient id="teamTone" x1="0" x2="1" y1="0" y2="1">
        <stop offset="0" stop-color="#e8b53a"/>
        <stop offset="0.5" stop-color="#4a6aa8"/>
        <stop offset="1" stop-color="#e8743a"/>
      </linearGradient>
    </defs>
    <path d="M0 0 H1200 V3 C1000 100 700 170 0 197 Z" fill="var(--navy)"/>
    <path d="M0 207 C500 200 800 150 1071 70 C820 160 500 240 0 256 Z" fill="var(--red)"/>
    <path d="M880 520 C1000 470 1100 450 1200 424 V467 C1100 480 1000 500 880 530 Z" fill="var(--red)"/>
    <rect role="img" aria-label="Foto: drei Fachkräfte mit Schutzhelm und Warnweste, Arme verschränkt" x="845" y="282" width="295" height="215" fill="url(#teamTone)" opacity="0.5"/>
    <path d="M640 585 C800 520 1000 490 1200 467 V474 C1000 495 800 525 660 580 Z" fill="var(--red)"/>
    <path d="M562 602 C750 520 1000 490 1200 474 V602 Z" fill="var(--red)"/>
    <path d="M590 602 C780 525 1000 495 1200 479 V602 Z" fill="var(--navy)"/>
    <path d="M103 602 C180 575 300 570 400 602 Z" fill="var(--red)"/>
    <path d="M103 602 C170 578 270 574 365 602 Z" fill="var(--navy)"/>
  </svg>

  <div class="brand"><span class="brand-dot"></span>stahlwerk Akademie</div>
  <div class="tagline">Hier wächst echtes Sicherheitswissen!</div>

  <div class="contact">
    <div class="contact-row">
      <svg class="contact-icon" viewBox="0 0 24 24"><path d="M6.6 10.8a15 15 0 0 0 6.6 6.6l2.2-2.2a1 1 0 0 1 1-.25 11.4 11.4 0 0 0 3.6.57 1 1 0 0 1 1 1V20a1 1 0 0 1-1 1A17 17 0 0 1 3 4a1 1 0 0 1 1-1h3.5a1 1 0 0 1 1 1c0 1.25.2 2.45.57 3.57a1 1 0 0 1-.25 1z"/></svg>
      <span>+49 1701 2345 67</span>
    </div>
    <div class="contact-row">
      <svg class="contact-icon" viewBox="0 0 24 24"><path d="M12 2a10 10 0 1 0 5 18.7l-1-1.7A8 8 0 1 1 20 12v1.2a1.8 1.8 0 0 1-3.6 0V7h-2v1a5 5 0 1 0 .7 7.1A3.8 3.8 0 0 0 22 13.2V12A10 10 0 0 0 12 2zm0 13a3 3 0 1 1 0-6 3 3 0 0 1 0 6z"/></svg>
      <span>kurse@lindenfeld-schulung.de</span>
    </div>
    <div class="contact-row">
      <svg class="contact-icon" viewBox="0 0 24 24"><path d="M12 2a7 7 0 0 0-7 7c0 5.2 7 13 7 13s7-7.8 7-13a7 7 0 0 0-7-7zm0 9.5A2.5 2.5 0 1 1 12 6.5a2.5 2.5 0 0 1 0 5z"/></svg>
      <span>stahlwerk Akademie UG<br>Lindenweg 12<br>91190 Feldhausen</span>
    </div>
  </div>

  <div class="claim">
    Sicherheit <span class="accent">und Kompetenz</span><br>am Arbeitsplatz
  </div>
</div>
</body>
</html>
```